Kowhai Crest (Podiatry and Physiotherapy) Clinical Brochure

You are producing a brochure that will sit in clinical/medical waiting rooms for our business Kowhai Crest. A clinic that providers podiatry and physiotherapy services.

As you can see on our website www.kowhaicrest.example.nz we provide 6 different brands/services:
- Clearbloom Care
- Brightedge Relief Studio
- Stepsure Works
- Riverstone Motion Renewal
- Pearlgleam Studio
- Tidewater Everyday Care

People will generally have found us through an ad e.g. search fungal nail treatment and end up straight on www.clearbloomcare.example.nz and therefore, each of the brands should be seen as being separate entities although part of the bigger brand Kowhai Crest.

We are looking at a brochure (open to bi-fold, tri-fold etc.) that highlights all of our brands as well as the services that each of our brands provide which can be found on each of the websites listed above. We want this to be professional and informative yet simple and easy to read - this interpretation can be somewhat left up to you. This brochure will sit in waiting rooms/clinical environments.

I have attached our brand strategy so that you can understand our fonts and colours. I have also attached our logos for reference.

```html
<!DOCTYPE html>
<html lang="en">
<head>
<meta charset="utf-8">
<title>Kowhai Crest – Clinical Brochure Inside Spread</title>
<link href="https://fonts.googleapis.com/css2?family=Arimo:wght@400;700&display=swap" rel="stylesheet">
<style>
  :root {
    --brand-blue: #2f74c0;
    --ink: #444;
    --ink-dark: #333;
    --white: #fff;
    --panel-dark-1: #2b2b2e;
    --panel-dark-2: #4a4644;
    --panel-light-1: #eef0f2;
    --panel-light-2: #f9f9f9;
    --skin-1: #f1d6c6;
    --skin-2: #fbf4f0;
  }
  * { margin: 0; padding: 0; box-sizing: border-box; }
  html, body { width: 1200px; height: 848px; overflow: hidden; background: var(--white); }
  body { font-family: "Arimo", Arial, sans-serif; }
  .spread { position: relative; width: 1200px; height: 848px; overflow: hidden; }
  .panel { position: absolute; top: 0; width: 400px; height: 848px; }
  .panel--about { left: 0; background: var(--white); }
  .panel--treatments { left: 400px; background: linear-gradient(160deg, var(--panel-dark-1) 0%, #38332f 55%, var(--panel-dark-2) 100%); }
  .panel--team { left: 800px; background: linear-gradient(180deg, var(--panel-light-1) 0%, var(--panel-light-2) 60%, #f3ece7 100%); }

  .photo-legs { position: absolute; left: 40px; top: 0; width: 240px; height: 312px;
    background: radial-gradient(ellipse at 50% 45%, var(--skin-1) 0%, var(--skin-2) 60%, var(--white) 100%); }
  .photo-feet { position: absolute; left: 80px; top: 620px; width: 320px; height: 228px;
    background: radial-gradient(ellipse at 55% 70%, #e9c7b3 0%, #f3e1d6 55%, rgba(249,249,249,0) 100%); }

  .heading { position: absolute; font-weight: 700; font-size: 28px; white-space: nowrap; }
  .heading--blue { color: var(--brand-blue); }
  .heading--white { color: var(--white); }

  .about-text { position: absolute; left: 41px; top: 404px; font-size: 17.5px; line-height: 25.5px; color: var(--ink); white-space: nowrap; }
  .services-intro { position: absolute; left: 41px; top: 635px; font-size: 15px; font-weight: 700; color: var(--ink-dark); }
  .bullet-list { position: absolute; list-style: none; }
  .bullet-list li { position: relative; padding-left: 27px; font-size: 15px; line-height: 24.7px; white-space: nowrap; }
  .bullet-list li::before { content: "•"; position: absolute; left: 0; }
  .services-list { left: 41px; top: 657px; color: var(--ink); }

  .treatment { position: absolute; left: 445px; color: var(--white); white-space: nowrap; }
  .treatment h3 { font-size: 17px; font-weight: 700; margin-bottom: 6px; }
  .treatment p { font-size: 14.5px; line-height: 20.5px; }
  .thumb { position: absolute; left: 649px; width: 114px; height: 88px; border-radius: 8px; border: 1px solid rgba(255,255,255,.6); }
  .extra-title { position: absolute; left: 445px; top: 650px; color: var(--white); font-size: 15px; font-weight: 700; }
  .extra-list { left: 445px; top: 671px; color: var(--white); }

  .member { position: absolute; left: 845px; color: var(--ink-dark); font-size: 15px; line-height: 20.5px; white-space: nowrap; }
  .member strong { display: block; font-weight: 700; }
  .portrait { position: absolute; left: 1046px; width: 113px; height: 88px; border-radius: 8px; background: linear-gradient(180deg, #dcd7d0, #cfc8bf); }
</style>
</head>
<body>
<main class="spread">

  <section class="panel panel--about">
    <div class="photo-legs" role="img" aria-label="Photo of bare feet and lower legs"></div>
    <h2 class="heading heading--blue" style="left:41px;top:346px;">About us</h2>
    <p class="about-text">The Kowhai Crest team of highly trained<br>and experienced podiatrists and<br>physiotherapists provide preventative<br>care, management strategies and<br>rehabilitation services for foot,<br>ankle or lower leg problems.</p>
    <h2 class="heading heading--blue" style="left:41px;top:580px;">Our Services</h2>
    <p class="services-intro">We provide solutions through:</p>
    <ul class="bullet-list services-list">
      <li>Clearbloom Care</li>
      <li>Brightedge Relief Studio</li>
      <li>Stepsure Works</li>
      <li>Riverstone Motion Renewal</li>
      <li>Pearlgleam Studio</li>
      <li>Tidewater Everyday Care</li>
    </ul>
  </section>

  <section class="panel panel--treatments" role="img" aria-label="Dim photo of people walking on a beach behind the treatments list"></section>
  <h2 class="heading heading--white" style="left:445px;top:100px;">Our treatments</h2>

  <article class="treatment" style="top:154px;">
    <h3>Lumora Cold Laser</h3>
    <p>Lumora cold laser is a pain-<br>free, non-thermal laser that<br>requires no anaesthetic.</p>
  </article>
  <div class="thumb" style="top:178px;background:linear-gradient(135deg,#e8e6e3,#c96a6a);" role="img" aria-label="Photo of a foot under a cold laser device"></div>

  <article class="treatment" style="top:261px;">
    <h3>Microvent</h3>
    <p>Microvent treatment<br>produces micro holes<br>through the nail for high<br>concentration medication<br>to reach the infection.</p>
  </article>
  <div class="thumb" style="top:300px;background:linear-gradient(135deg,#f6f6f6,#e6cfc2);" role="img" aria-label="Photo of a nail drilling tool on a foot"></div>

  <article class="treatment" style="top:410px;">
    <h3>Photodisinfection</h3>
    <p>A new, safe and effective<br>in-clinic treatment for<br>onychomycosis (fungal nails).</p>
  </article>
  <div class="thumb" style="top:420px;background:linear-gradient(90deg,#1d3342,#7fd6e6 50%,#1d3342);" role="img" aria-label="Photo of blue ultraviolet treatment lamps"></div>

  <article class="treatment" style="top:516px;">
    <h3>Nailform Nail Restoration</h3>
    <p>A painless, in-office<br>application that restores<br>the appearance of an<br>individual's natural nails.</p>
  </article>
  <div class="thumb" style="top:542px;background:linear-gradient(135deg,#e3bfae,#c99a88);" role="img" aria-label="Before and after photos of restored toenails"></div>

  <p class="extra-title">We also provide:</p>
  <ul class="bullet-list extra-list">
    <li>Topical Treatments</li>
    <li>Oral Treatments</li>
    <li>Surgery</li>
    <li>General Nail Care</li>
    <li>Arcline Nail Bracing</li>
  </ul>
  <div class="thumb" style="top:662px;background:linear-gradient(135deg,#eaf4fb,#3a8fd0);" role="img" aria-label="Photo of a gloved hand treating a toe"></div>

  <section class="panel panel--team" role="img" aria-label="Faded photo of a couple walking on the beach">
    <div class="photo-feet" role="img" aria-label="Photo of bare toes"></div>
  </section>
  <h2 class="heading heading--blue" style="left:845px;top:100px;">Meet our team</h2>

  <p class="member" style="top:151px;"><strong>Daniel Marsh</strong>Co-Director<br>Lead Clinician<br>(Podiatrist/Physiotherapist)</p>
  <div class="portrait" style="top:178px;" role="img" aria-label="Portrait of Daniel Marsh"></div>

  <p class="member" style="top:279px;"><strong>Megan Ashford-Reid</strong>Co-Director<br>Clinician<br>(Nurse)</p>
  <div class="portrait" style="top:299px;" role="img" aria-label="Portrait of Megan Ashford-Reid"></div>

  <p class="member" style="top:406px;"><strong>Ingrid Fowler</strong>Clinician<br>(Podiatrist)</p>
  <div class="portrait" style="top:420px;" role="img" aria-label="Portrait of Ingrid Fowler"></div>

  <p class="member" style="top:513px;"><strong>Liam Prescott</strong>Clinician<br>(Podiatrist)</p>
  <div class="portrait" style="top:541px;" role="img" aria-label="Portrait of Liam Prescott"></div>

</main>
</body>
</html>
```